Brellmoor Cosmetic Doctor is the title and the name of the business

Facebook advertising: keep
To those dimensions

Aimed at Caucasian women between the ages of 18 - 60 interested in beauty and cosmetic injectables. Will be boosted on facebook which is my advertising platform.

Name: Brellmoor Cosmetic Doctor
0400 555 271

Forehead $58
Frown lines $116
Crows feet $116
Lip fillers $380

I would like to have a beautiful girl that suits the picture.

Target Market(s)

Females between 18 - 60 interested in Lumarex and cosmetic fillers
Prefer Caucasian as that's the majority of population

Industry/Entity Type

Beauty Salon

Font styles to use
Serif
Script

Colors
e667a6
eea4c8
f9d9e8
fee18a
fbf289
fbee3d
cadf82
cedeed
85cae6

Requirements
Must have
• Name: Brellmoor Cosmetic Doctor
• Phone number: 0400 559 271
• Prices:
• Forehead $58
• Frown lines $116
• Crows feet $116
• Lip fillers $380
• Picture of female that is very beautiful
Nice to have
• Not a cartoon or anything else that's not a real picture of a female
Should not have
• No cartoon pictures. Proper picture of women

```html
<!DOCTYPE html>
<html lang="en">
<head>
<meta charset="utf-8">
<title>Brellmoor Cosmetic Doctor – Facebook Ad</title>
<link rel="stylesheet" href="https://fonts.googleapis.com/css2?family=Federant&display=swap">
<style>
  :root {
    --page-bg: #ffffff;
    --ad-bg: #0b0c0f;
    --band: #7a0f73;
    --cream: #f8e6c9;
    --white: #ffffff;
    --forehead: #d3137e;
    --frown: #cf0530;
    --crows: #a0426b;
    --lips: #d8646c;
    --skin-light: #efd8c8;
    --skin-mid: #d9b3a0;
    --hair: #4a3a33;
    --violet: #8a2bb8;
  }
  html, body {
    margin: 0;
    width: 1200px;
    height: 903px;
    overflow: hidden;
    background: var(--page-bg);
  }
  .ad {
    position: absolute;
    left: 157px;
    top: 288px;
    width: 888px;
    height: 328px;
    background: var(--ad-bg);
    overflow: hidden;
    box-shadow: 2px 3px 5px rgba(0,0,0,.35);
    font-family: "Federant", Georgia, serif;
    color: var(--cream);
  }
  .model-photo {
    position: absolute;
    right: 0;
    top: 0;
    width: 272px;
    height: 100%;
    background:
      radial-gradient(ellipse 45% 40% at 60% 45%, var(--skin-light), transparent 75%),
      radial-gradient(ellipse 40% 30% at 55% 90%, var(--violet), transparent 70%),
      linear-gradient(90deg, rgba(11,12,15,0) 0%, var(--hair) 14%, var(--skin-mid) 42%, var(--skin-light) 100%);
  }
  .price-cloud {
    position: absolute;
    filter: drop-shadow(0 0 7px rgba(255,240,240,.55));
  }
  .price-cloud svg {
    position: absolute;
    inset: 0;
    width: 100%;
    height: 100%;
  }
  .treatment, .price {
    position: absolute;
    transform: translate(-50%, -50%);
    white-space: nowrap;
    line-height: 1;
    text-shadow: 1px 2px 2px rgba(0,0,0,.45);
  }
  .treatment { font-size: 33px; }
  .price { font-size: 41px; }

  .cloud-forehead { left: 7px;   top: 9px;   width: 223px; height: 141px; }
  .cloud-forehead .treatment { left: 102px; top: 63px; }
  .cloud-forehead .price     { left: 96px;  top: 110px; }

  .cloud-frown { left: 281px; top: 9px; width: 222px; height: 130px; }
  .cloud-frown .treatment { left: 109px; top: 60px; }
  .cloud-frown .price     { left: 109px; top: 101px; }

  .cloud-crows { left: 145px; top: 127px; width: 221px; height: 140px; }
  .cloud-crows .treatment { left: 98px; top: 59px; }
  .cloud-crows .price     { left: 98px; top: 103px; }

  .cloud-lips { left: 411px; top: 145px; width: 223px; height: 104px; }
  .cloud-lips .treatment { left: 100px; top: 36px; }
  .cloud-lips .price     { left: 100px; top: 78px; }

  .book-today {
    position: absolute;
    left: 330px;
    top: 246px;
    font-size: 17px;
    line-height: 20px;
    white-space: nowrap;
    color: var(--white);
  }
  .contact-band {
    position: absolute;
    left: 0;
    top: 279px;
    width: 620px;
    height: 49px;
    background: var(--band);
    color: var(--white);
    font-size: 23px;
    line-height: 49px;
  }
  .business-name, .phone, .band-dot {
    position: absolute;
    white-space: nowrap;
  }
  .business-name { left: 40px; top: 0; }
  .band-dot {
    left: 390px;
    top: 20px;
    width: 9px;
    height: 9px;
    border-radius: 50%;
    background: var(--cream);
  }
  .phone { left: 440px; top: 0; }
</style>
</head>
<body>
  <section class="ad">
    <div class="model-photo" role="img" aria-label="Photograph of a beautiful woman with violet makeup and nails, hand resting in her hair"></div>

    <div class="price-cloud cloud-forehead">
      <svg viewBox="0 0 220 140" preserveAspectRatio="none"><path fill="var(--forehead)" d="M30,122 C5,122 2,88 20,78 C4,56 24,30 50,40 C56,14 88,4 108,20 C128,0 170,6 176,36 C206,38 220,68 202,88 C220,108 198,132 174,124 C158,140 112,140 96,126 C76,138 46,136 30,122 Z"/></svg>
      <span class="treatment">Forehead</span><span class="price">$58</span>
    </div>

    <div class="price-cloud cloud-frown">
      <svg viewBox="0 0 220 140" preserveAspectRatio="none"><path fill="var(--frown)" d="M30,122 C5,122 2,88 20,78 C4,56 24,30 50,40 C56,14 88,4 108,20 C128,0 170,6 176,36 C206,38 220,68 202,88 C220,108 198,132 174,124 C158,140 112,140 96,126 C76,138 46,136 30,122 Z"/></svg>
      <span class="treatment">Frown lines</span><span class="price">$116</span>
    </div>

    <div class="price-cloud cloud-crows">
      <svg viewBox="0 0 220 140" preserveAspectRatio="none"><path fill="var(--crows)" d="M30,122 C5,122 2,88 20,78 C4,56 24,30 50,40 C56,14 88,4 108,20 C128,0 170,6 176,36 C206,38 220,68 202,88 C220,108 198,132 174,124 C158,140 112,140 96,126 C76,138 46,136 30,122 Z"/></svg>
      <span class="treatment">Crows feet</span><span class="price">$116</span>
    </div>

    <div class="price-cloud cloud-lips">
      <svg viewBox="0 0 220 140" preserveAspectRatio="none"><path fill="var(--lips)" d="M30,122 C5,122 2,88 20,78 C4,56 24,30 50,40 C56,14 88,4 108,20 C128,0 170,6 176,36 C206,38 220,68 202,88 C220,108 198,132 174,124 C158,140 112,140 96,126 C76,138 46,136 30,122 Z"/></svg>
      <span class="treatment">Lip fillers</span><span class="price">$380</span>
    </div>

    <div class="book-today">Book Today</div>

    <div class="contact-band">
      <span class="business-name">Brellmoor Cosmetic Doctor</span>
      <span class="band-dot" aria-hidden="true"></span>
      <span class="phone">0400559271</span>
    </div>
  </section>
</body>
</html>
```